Business Consulting Website Design

UPDATED KEY MESSAGES:

The client has decided o a different direction.

The Key Messages include:
-- Creating something unique.
Every company is unique, ever culture unique. Every project customized to meet the unique needs of the client. No two things are alike.
-- One of a kind
Because every company is different, every culture is different, every objective is unique
-- Customized solutions
We create something just for you …

I think the approach needs to be about creating a masterpiece as opposed to nurturing/growing.

Perhaps we could have different abstract/colorful paint items that takes up part of the page for each landing page. Against white and on the white is where we put our text.

Client also has created a Pixelgrove Lightbox with images that she likes

http://www.pixelgrove-example.com/public_board.mhtml?code=a7c2e9f04b8d13562e7f90a1c4d6b852&board_id=58217409

She also likes the watercolor look against white background.

===============================
Need a Homepage and an Interior page redesign for my client: http://www.brightwavecounsel-example.com

Client does leadership development, performance management, talent development, etc. Has some great clients.

- This site is very old and needs a modern look. Update look & colors. She wants simple but not bland.
- Banner images should be interesting.
- She likes the purple in her logo
- She thinks Arial font is outdated and boring
- We will be rewriting all the copy.
- Design should include ProLinker icon, phone, email, and address
- She likes the client grid on the Our Clients page. We will be redoing this.

- Menus will include:
-- Home
-- What We Do
-- Who We Are
-- Our Clients
-- Snapshots (these are case studies)

One of the sites she liked is http://lanternfold-novel-example.com, though this website has much more content than she will have.

I'm attaching the following files for your reference:
- Her new business card proof that contains her logo
- a zip file containing some stock image comps

Need strong design. Site will likely be built in Wordpress.

Thanks,
Nora
Updates

Target Market(s)

SVP of Human Resources or Head of Talent

Industry/Entity Type

Business

Number of Pages Required

2 page

Font styles to use
Sans Serif

Colors
b768aa
876aae
6b449b
f04a50
f37122

Requirements
Must have
• - Designer must read the brief
• - Use logo
Nice to have
• - Strong banner images to complement the key message
• - Design will function work on mobile easily
Should not have
• - Should not look like a design template was purchased from layoutbazaar-example.com or other template sites.
• - Should not be too masculine
• - Should not feel cluttered.

```html
<!DOCTYPE html>
<html lang="en">
<head>
<meta charset="utf-8">
<title>Brightwave Counsel — Home</title>
<link href="https://fonts.googleapis.com/css2?family=Work+Sans:wght@200;300;400;600&family=Montserrat:wght@600&display=swap" rel="stylesheet">
<style>
  :root {
    --orchid: #b768aa;
    --lavender: #876aae;
    --purple: #6b449b;
    --coral: #f04a50;
    --orange: #f37122;
    --ink: #111111;
    --muted: #555555;
    --paper: #ffffff;
  }
  * { margin: 0; padding: 0; box-sizing: border-box; }
  html, body { width: 1200px; height: 750px; overflow: hidden; }
  body { position: relative; font-family: "Work Sans", sans-serif; color: var(--ink); background: var(--paper); }

  .watercolour-wash {
    position: absolute; inset: 0;
    background:
      radial-gradient(ellipse 300px 260px at 1120px 200px, rgba(183,104,170,0.42) 0%, rgba(183,104,170,0.16) 50%, rgba(183,104,170,0) 75%),
      radial-gradient(ellipse 240px 220px at 990px 420px, rgba(135,106,174,0.34) 0%, rgba(135,106,174,0) 72%),
      radial-gradient(ellipse 220px 200px at 1140px 560px, rgba(240,74,80,0.26) 0%, rgba(240,74,80,0) 72%),
      radial-gradient(ellipse 260px 240px at 70px 470px, rgba(107,68,155,0.30) 0%, rgba(107,68,155,0) 72%),
      radial-gradient(ellipse 200px 180px at 180px 640px, rgba(243,113,34,0.20) 0%, rgba(243,113,34,0) 72%),
      var(--paper);
  }

  .nav-marker { position: absolute; left: 64px; top: 0; width: 51px; height: 99px; background: var(--coral); }
  .main-nav {
    position: absolute; left: 64px; top: 26px; width: 518px; height: 23px;
    display: flex; justify-content: space-between; padding: 0 4px 0 6px;
    border-bottom: 1px solid var(--orange);
  }
  .main-nav a {
    font-weight: 600; font-size: 14.5px; line-height: 20px;
    color: var(--ink); text-decoration: none; white-space: nowrap;
  }

  .social-links { position: absolute; top: 22px; left: 1025px; display: flex; gap: 10px; }
  .social-links span { width: 22px; height: 22px; background: var(--ink); border-radius: 2px; display: block; }

  .brand { position: absolute; left: 300px; top: 80px; width: 600px; text-align: center; }
  .brand-square { width: 64px; height: 64px; background: var(--purple); margin: 30px auto 64px; }
  .brand-name {
    font-family: "Montserrat", sans-serif; font-weight: 600; font-size: 54px;
    letter-spacing: 10px; line-height: 1.2; color: var(--purple); text-transform: uppercase;
  }

  .tagline-row {
    position: absolute; top: 562px; left: 168px; width: 845px;
    display: flex; align-items: center; gap: 18px;
  }
  .tagline-rule { flex: 1; height: 4px; background: var(--coral); border-radius: 2px; margin-top: 8px; }
  .tagline { font-weight: 200; font-size: 54px; letter-spacing: -1.5px; line-height: 66px; white-space: nowrap; }

  .cta {
    position: absolute; left: 515px; top: 648px; width: 182px; height: 39px;
    border: 1px solid var(--coral); border-radius: 5px; background: rgba(255,255,255,0.6);
    font-weight: 300; font-size: 25px; line-height: 37px; text-align: center;
    color: var(--ink); text-decoration: none; letter-spacing: -0.5px;
  }

  .contact-bar {
    position: absolute; top: 712px; left: 0; width: 1200px;
    display: flex; justify-content: center; gap: 34px;
    font-size: 13px; font-weight: 400; color: var(--muted);
  }
  .contact-item { display: flex; align-items: center; gap: 7px; }
  .contact-item svg { width: 14px; height: 14px; fill: none; stroke: var(--purple); stroke-width: 2; }
</style>
</head>
<body>
  <div class="watercolour-wash" role="img" aria-label="Soft purple, orchid and coral watercolour blooms on white"></div>

  <div class="nav-marker"></div>
  <nav class="main-nav">
    <a href="#">Home</a>
    <a href="#">What We Do</a>
    <a href="#">Who We Are</a>
    <a href="#">Our Clients</a>
    <a href="#">Snapshots</a>
    <a href="#">Contacts</a>
  </nav>

  <div class="social-links">
    <span aria-label="Photo network"></span>
    <span aria-label="Short-post network"></span>
    <span aria-label="Social network"></span>
    <span aria-label="Pinboard network"></span>
    <span aria-label="ProLinker"></span>
  </div>

  <div class="brand">
    <div class="brand-square"></div>
    <div class="brand-name">Brightwave<br>Counsel</div>
  </div>

  <div class="tagline-row">
    <div class="tagline-rule"></div>
    <h1 class="tagline">Realize Potential</h1>
    <div class="tagline-rule"></div>
  </div>

  <a class="cta" href="#">GET STARTED</a>

  <footer class="contact-bar">
    <span class="contact-item">
      <svg viewBox="0 0 24 24"><path d="M5 3h4l2 5-3 2a12 12 0 0 0 6 6l2-3 5 2v4a2 2 0 0 1-2 2A18 18 0 0 1 3 5a2 2 0 0 1 2-2z"/></svg>
      (555) 014-2378
    </span>
    <span class="contact-item">
      <svg viewBox="0 0 24 24"><rect x="3" y="5" width="18" height="14" rx="2"/><path d="M3 7l9 6 9-6"/></svg>
      hello@brightwavecounsel-example.com
    </span>
    <span class="contact-item">
      <svg viewBox="0 0 24 24"><path d="M12 22s7-7 7-12a7 7 0 0 0-14 0c0 5 7 12 7 12z"/><circle cx="12" cy="10" r="2.5"/></svg>
      240 Lantern Row, Suite 5, Fairhaven
    </span>
  </footer>
</body>
</html>
```